Swimming Pool Supply Company Business Cards

We need business cards designed for company. These need to be easy to edit so that we can fill in names, titles, and contact info for each person who works here.

Dalton R. Whitfield
Manager of Legal & Finance
K.L. Brisbane, Incorporated

4837 Grenway Avenue
Marlow Heights, PA 19243

E. dalton@klbrisbane-example.com
M. (215) 555-0173
O. (215) 555-0148

Contact Information for Business Card

Looking to upgrade current business cards with graphic that can be edited. Looking for fresh ideas for an age old industry.

Font styles to use
Serif
Sans Serif

Colors

Designer to choose colors to be used in the design.

Requirements
Must have
• Professional, fresh, unique but professional

```html
<!DOCTYPE html>
<html lang="en">
<head>
<meta charset="utf-8">
<title>Business Card – Front and Back</title>
<link rel="stylesheet" href="https://fonts.googleapis.com/css2?family=Source+Sans+3:wght@400;600;700;800&display=swap">
<style>
  :root {
    --brand-blue: #0040ff;
    --paper: #ffffff;
    --ink: #000000;
    --edge: #1a1a1a;
  }
  * { box-sizing: border-box; margin: 0; padding: 0; }
  html, body {
    width: 1161px; height: 1200px; overflow: hidden;
    background: var(--paper);
    font-family: "Source Sans 3", "Segoe UI", sans-serif;
  }
  .sheet { position: relative; width: 1161px; height: 1200px; }

  .card {
    position: absolute; left: 1px; width: 949px; height: 557px;
    border: 1.5px solid var(--edge);
    border-radius: 52px 0 52px 0;
    overflow: hidden;
  }
  .card--front { top: 1px; background: var(--brand-blue); }
  .card--back { top: 640px; background: var(--brand-blue); }

  .side-label {
    position: absolute; left: 1017px; color: var(--ink);
    font-size: 62px; font-weight: 400; line-height: 1;
  }
  .side-label--front { top: 296px; }
  .side-label--back { top: 830px; left: 997px; }

  /* front */
  .brand-panel {
    position: absolute; left: 0; top: 0; width: 300px; height: 100%;
    background: var(--paper);
    border-right: 1px solid var(--edge);
  }
  .brand-panel__mark, .brand-panel__company {
    position: absolute; writing-mode: vertical-rl; transform: rotate(180deg);
    color: var(--brand-blue); white-space: nowrap;
  }
  .brand-panel__mark {
    left: 78px; top: 52px; height: 454px;
    font-size: 92px; font-weight: 800; line-height: 1;
    text-align: center; letter-spacing: -2px;
  }
  .brand-panel__company {
    left: 196px; top: 64px; height: 430px;
    font-size: 30px; font-weight: 600; line-height: 1;
    text-align: left;
  }

  .person { position: absolute; left: 377px; top: 74px; color: var(--paper); }
  .person__row { display: flex; align-items: flex-start; gap: 39px; }
  .person__name { font-size: 33px; font-weight: 700; line-height: 1.05; }
  .person__title { font-size: 22px; font-weight: 400; margin-top: 2px; }

  .contact-list {
    position: absolute; left: 377px; top: 260px; list-style: none;
    color: var(--paper); font-size: 25px; line-height: 1.2;
  }
  .contact-list li { display: flex; align-items: flex-start; gap: 39px; margin-bottom: 17px; }
  .icon-tile {
    flex: none; width: 31px; height: 31px; background: var(--paper);
    display: flex; align-items: center; justify-content: center; margin-top: 1px;
  }
  .icon-tile svg { width: 24px; height: 24px; }

  /* back */
  .back-brand {
    position: absolute; left: 0; right: 0; top: 178px; text-align: center;
    color: var(--paper);
  }
  .back-brand__name {
    font-size: 168px; font-weight: 800; line-height: 1; letter-spacing: -3px;
  }
  .back-brand__tagline {
    font-size: 33px; font-weight: 400; margin-top: 14px;
  }
</style>
</head>
<body>
<div class="sheet">

  <section class="card card--front" aria-label="Card front">
    <div class="brand-panel">
      <div class="brand-panel__mark">BRISBANE</div>
      <div class="brand-panel__company">K.L. Brisbane, Incorporated</div>
    </div>

    <div class="person">
      <div class="person__row">
        <span class="icon-tile" aria-hidden="true">
          <svg viewBox="0 0 24 24"><circle cx="12" cy="9" r="5" fill="#0040ff"/><path d="M3 23c0-6 4-9 9-9s9 3 9 9z" fill="#0040ff"/></svg>
        </span>
        <div>
          <div class="person__name">Dalton R. Whitfield</div>
          <div class="person__title">Manager of Legal &amp; Finance</div>
        </div>
      </div>
    </div>

    <ul class="contact-list">
      <li>
        <span class="icon-tile" aria-hidden="true">
          <svg viewBox="0 0 24 24"><path d="M8 3c-2 1-3 3-2 7s4 9 7 11c2 1 3 0 4-1l-3-4-2 1c-2-2-3-5-3-7l2-1z" fill="none" stroke="#0040ff" stroke-width="1.6"/></svg>
        </span>
        <span>(215) 555-0173</span>
      </li>
      <li>
        <span class="icon-tile" aria-hidden="true">
          <svg viewBox="0 0 24 24"><path d="M2 9c3-4 17-4 20 0l-3 2-2-2H7l-2 2z" fill="#0040ff"/><path d="M6 12h12l2 8H4z" fill="#0040ff"/><circle cx="12" cy="16" r="2.2" fill="#fff"/></svg>
        </span>
        <span>(215) 555-0148</span>
      </li>
      <li>
        <span class="icon-tile" aria-hidden="true">
          <svg viewBox="0 0 24 24"><rect x="3" y="6" width="18" height="12" fill="none" stroke="#0040ff" stroke-width="1.6"/><path d="M3 6l9 7 9-7" fill="none" stroke="#0040ff" stroke-width="1.6"/></svg>
        </span>
        <span>dalton@klbrisbane-example.com</span>
      </li>
      <li>
        <span class="icon-tile" aria-hidden="true">
          <svg viewBox="0 0 24 24"><path d="M12 19s-6-6-6-10a6 6 0 0 1 12 0c0 4-6 10-6 10z" fill="none" stroke="#0040ff" stroke-width="1.8"/><circle cx="12" cy="9" r="2" fill="#0040ff"/><ellipse cx="12" cy="21" rx="5" ry="1.3" fill="#0040ff"/></svg>
        </span>
        <span>4837 Grenway Avenue<br>Marlow Heights, PA 19243</span>
      </li>
    </ul>
  </section>

  <p class="side-label side-label--front">Front</p>

  <section class="card card--back" aria-label="Card back">
    <div class="back-brand">
      <div class="back-brand__name">BRISBANE</div>
      <div class="back-brand__tagline">Big Enough to Serve You, Small Enough to Care</div>
    </div>
  </section>

  <p class="side-label side-label--back">Back</p>

</div>
</body>
</html>
```